Odvetnik - Attorney at law
Sodni tolmač za angleški jezik - English language Court Interpreter
Simple
Marjan Lesk
Odvetnik - Attorney at law Sodni tolmač za angleški jezik - English Language Court Interpreter
Brinjeva ulica 41 6000 Koper Slovenija
info@marjanlesk.example
www.marjanlesk.example
I invite all designers under logo project Attorney Marjan Lesk to participate. Please inform all designers.

```html
<!DOCTYPE html>
<html lang="sl">
<head>
<meta charset="utf-8">
<title>Marjan Lesk – Business Card</title>
<link rel="stylesheet" href="https://fonts.googleapis.com/css2?family=Open+Sans:wght@400;600;700&display=swap">
<style>
  :root {
    --backdrop: #3b3b3b;
    --card: #ffffff;
    --navy: #2d3584;
    --ink: #2f2f2f;
    --accent: #e8672c;
    --rule: #8c8fb8;
  }
  * { margin: 0; padding: 0; box-sizing: border-box; }
  html, body { width: 1200px; height: 746px; overflow: hidden; }
  body {
    background: var(--backdrop);
    font-family: "Open Sans", Arial, sans-serif;
    position: relative;
  }
  .card {
    position: absolute;
    left: 235px; top: 163px;
    width: 727px; height: 403px;
    background: var(--card);
  }
  .brand {
    position: absolute;
    left: 22px; top: 168px;
    width: 320px;
  }
  .brand-row { display: flex; align-items: center; gap: 10px; }
  .brand-mark {
    width: 38px; height: 38px; border-radius: 50%;
    background: var(--accent); flex: none;
  }
  .brand-name {
    font-size: 33px; font-weight: 400; letter-spacing: 1px;
    color: var(--navy); line-height: 1;
  }
  .brand-tagline {
    margin: 8px 0 0 50px;
    font-size: 15px; color: var(--accent);
  }
  .divider {
    position: absolute;
    left: 348px; top: 77px;
    width: 1px; height: 257px;
    background: var(--rule);
  }
  .details {
    position: absolute;
    left: 370px; top: 80px;
    color: var(--ink);
    font-size: 16.5px; line-height: 29px;
  }
  .details .person {
    font-size: 24px; font-weight: 600; color: var(--navy);
    line-height: 34px; margin-bottom: 0;
  }
  .details .role { line-height: 25px; }
  .details .contacts { margin-top: 6px; }
  .details .label { font-weight: 700; color: var(--navy); }
  .details .web { font-weight: 700; color: var(--navy); }
</style>
</head>
<body>
  <div class="card">
    <div class="brand">
      <div class="brand-row">
        <span class="brand-mark"></span>
        <span class="brand-name">MARJAN LESK</span>
      </div>
      <div class="brand-tagline">Odvetnik - Attorney at law</div>
    </div>

    <div class="divider"></div>

    <div class="details">
      <div class="person">Marjan Lesk</div>
      <div class="role">Odvetnik</div>
      <div class="role">Attorney at law Sodni tolmač za angleški jezik</div>
      <div class="role">English Language Court Interpreter</div>
      <div class="contacts">
        <div><span class="label">E:</span> info@marjanlesk.example</div>
        <div><span class="label">P:</span> +386 5 5550190</div>
        <div><span class="label">C:</span> +386 40555172</div>
        <div><span class="label">F:</span> +386 5 5550191</div>
        <div>Brinjeva ulica 41 6000 Koper Slovenija</div>
        <div class="web">www.marjanlesk.example</div>
      </div>
    </div>
  </div>
</body>
</html>
```